AI Maple Sprint Presentation

We have a wireframe presentation with 43 slides (many with the same format) to be implemented in Powerpoint. We provide Corporate presentation in order to reuse template. Please, be creative and don't take the examples in the wireframe as literal. We also provide the following:
- Color palette
- lumafox Logos
- Slide wireframe
- Flyer
- lumafox Corporate Presentation. Please, use this as a general template.
You can find all the materials here:
https://files.brenvale.net/shared/7QpLxZ2RtK9mVwB4nYcHs0JdFgE3aUoT?view=link

```html
<!DOCTYPE html>
<html lang="en">
<head>
<meta charset="utf-8">
<title>AI Maple Sprint – Presentation Slides</title>
<link rel="stylesheet" href="https://fonts.googleapis.com/css2?family=Montserrat:wght@700;800&family=Inter:wght@300;400&display=swap">
<style>
  :root {
    --navy: #04253a;
    --navy-deep: #031c2d;
    --teal: #2aa59a;
    --teal-soft: #4f9f98;
    --olive: #a09030;
    --stone: #8b8f8f;
    --white: #ffffff;
    --page: #ffffff;
  }
  * { margin: 0; padding: 0; box-sizing: border-box; }
  html, body { width: 1004px; height: 1200px; overflow: hidden; background: var(--page); }
  .canvas { position: relative; width: 1004px; height: 1200px; }
  .slide {
    position: absolute; width: 442px; height: 249px;
    background: var(--navy); overflow: hidden; color: var(--white);
    font-family: 'Inter', sans-serif;
  }
  .brand { display: inline-flex; align-items: center; gap: 0.22em; }
  .brand-mark { width: 0.62em; height: 0.62em; background: var(--teal); }
  .brand-name { font-family: 'Montserrat', sans-serif; font-weight: 700; color: var(--white); letter-spacing: -0.02em; line-height: 1; }
  .slide-header { position: absolute; left: 15px; top: 12px; display: flex; align-items: center; height: 28px; }
  .slide-header .brand { font-size: 20px; }
  .header-divider { width: 1px; height: 27px; background: var(--white); margin: 0 14px 0 16px; opacity: .8; }
  .header-title { font-family: 'Montserrat', sans-serif; font-weight: 700; font-size: 12.5px; }
  .photo { position: absolute; border-radius: 50%; }

  /* Title slide */
  .title-slide .brand { position: absolute; left: 28px; top: 30px; font-size: 26px; }
  .title-slide h1 { position: absolute; left: 28px; top: 100px; font-family: 'Montserrat', sans-serif; font-weight: 800; font-size: 26px; line-height: 1.28; }
  .title-slide h1 .accent { color: var(--teal); display: block; }
  .title-slide .photo { left: 218px; top: 54px; width: 220px; height: 220px;
    background: radial-gradient(circle at 58% 45%, #2a8fa3 0%, #124a66 30%, #0a2f48 60%, #3a2420 100%); }

  /* Introductions */
  .intro .person { position: absolute; left: 22px; top: 53px; }
  .intro .person-name { font-family: 'Montserrat', sans-serif; font-weight: 700; font-size: 12px; }
  .intro .person-role { font-family: 'Montserrat', sans-serif; font-size: 10px; font-weight: 700; opacity: .95; }
  .intro .notes { position: absolute; left: 23px; top: 91px; width: 225px; }
  .intro .note { margin-bottom: 9px; }
  .intro .note h3 { font-family: 'Montserrat', sans-serif; font-weight: 700; font-size: 5.3px; margin-bottom: 3px; letter-spacing: .02em; }
  .intro .note p { font-size: 4.9px; line-height: 1.5; }
  .intro .portrait { position: absolute; right: 0; top: 0; width: 173px; height: 249px;
    background: linear-gradient(180deg, #c3cccf 0%, #a9b3b6 55%, #7f8a90 100%); }

  /* Centered slides */
  .centered { text-align: center; }
  .centered .brand { position: absolute; left: 50%; transform: translateX(-50%); top: 36px; font-size: 20px; }
  .about-us h2 { position: absolute; width: 100%; top: 92px; font-family: 'Montserrat', sans-serif; font-weight: 800; font-size: 19px; }
  .about-us .tagline { position: absolute; width: 100%; top: 131px; font-family: 'Montserrat', sans-serif; font-weight: 800; font-size: 15px; color: var(--teal); }
  .about-us .intro-copy { position: absolute; width: 100%; top: 162px; font-size: 8px; line-height: 1.6; }
  .workshop h2 { position: absolute; width: 100%; top: 75px; font-family: 'Montserrat', sans-serif; font-weight: 800; font-size: 12.5px; }
  .workshop .objective { position: absolute; width: 100%; top: 97px; font-size: 7.8px; line-height: 1.6; }
  .pillars { position: absolute; left: 64px; top: 144px; display: flex; gap: 9px; }
  .pillar { width: 98px; height: 76px; background: var(--teal); display: flex; flex-direction: column; align-items: center; justify-content: flex-start; padding-top: 14px; }
  .pillar svg { width: 30px; height: 28px; }
  .pillar span { margin-top: 8px; font-family: 'Montserrat', sans-serif; font-weight: 700; font-size: 8px; color: var(--navy); line-height: 1.2; }

  /* Agenda */
  .agenda-steps { position: absolute; left: 19px; top: 83px; display: flex; gap: 16px; }
  .step { width: 122px; height: 122px; border-radius: 50%; display: flex; flex-direction: column; align-items: center; justify-content: center; font-weight: 300; }
  .step strong { font-weight: 300; font-size: 21px; }
  .step small { font-size: 11px; margin-top: 6px; }
  .step.inspire { background: var(--olive); }
  .step.discover { background: var(--teal-soft); }
  .step.prioritize { background: var(--stone); }

  /* Definition slides */
  .definition .photo { width: 166px; height: 166px; }
  .definition .definition-text { position: absolute; font-weight: 300; font-size: 12.7px; line-height: 1.32; }
  .ai-def .photo { left: 30px; top: 63px; background: radial-gradient(circle at 50% 50%, #2fb6e6 0%, #137ab0 40%, #0a3d63 80%, #062b45 100%); }
  .ai-def .definition-text { left: 233px; top: 88px; width: 180px; }
  .ml-def .photo { left: 29px; top: 63px; background: radial-gradient(circle at 45% 55%, #2e6f86 0%, #174560 45%, #0b2a3d 80%, #071c2a 100%); }
  .ml-def .definition-text { left: 231px; top: 83px; width: 180px; }

  /* Closing */
  .closing { background: linear-gradient(180deg, #0a2c43 0%, #05233a 55%, #0c3550 80%, #072539 100%); }
  .closing .brand { position: absolute; left: 50%; transform: translateX(-50%); top: 52px; font-size: 46px; }
  .closing h2 { position: absolute; width: 100%; top: 124px; text-align: center; font-family: 'Montserrat', sans-serif; font-weight: 800; font-size: 35px; }
</style>
</head>
<body>
<main class="canvas">

  <section class="slide title-slide" style="left:46px; top:48px;">
    <div class="brand"><span class="brand-mark"></span><span class="brand-name">lumafox</span></div>
    <h1><span class="accent">AI Maple</span>Sprint</h1>
    <div class="photo" role="img" aria-label="Photo of a hand touching a glowing AI chip hologram above a laptop"></div>
  </section>

  <section class="slide intro" style="left:515px; top:48px;">
    <div class="slide-header">
      <div class="brand"><span class="brand-mark"></span><span class="brand-name">lumafox</span></div>
      <span class="header-divider"></span>
      <span class="header-title">Introductions</span>
    </div>
    <div class="person">
      <div class="person-name">Marcus</div>
      <div class="person-role">Sales manager</div>
    </div>
    <div class="notes">
      <div class="note"><h3>DEPARTMENT</h3><p>Leads regional accounts for the analytics team, aligning client goals with delivery plans and tracking results across each quarter. Works closely with engineers to shape proposals, manage budgets and keep every project moving on time.</p></div>
      <div class="note"><h3>ROI</h3><p>Expects measurable returns within the first year, with clear savings from automation and faster reporting. Success means lower manual effort, better forecasts and a simple way to compare the value of each proposed use case.</p></div>
      <div class="note"><h3>WORKSHOP EX[ECATIONS</h3><p>Hopes to leave the session with a short list of practical ideas, a shared view of priorities and clear next steps. Open to bold thinking, provided every option stays realistic for current data and team skills.</p></div>
    </div>
    <div class="portrait" role="img" aria-label="Portrait photo of the sales manager in a dark suit, arms crossed"></div>
  </section>

  <section class="slide centered about-us" style="left:51px; top:321px;">
    <div class="brand"><span class="brand-mark"></span><span class="brand-name">lumafox</span></div>
    <h2>About Us</h2>
    <p class="tagline">Data Analytics &amp; AI for Nonconformists</p>
    <p class="intro-copy">We are a leading Professional Services company specialized in the design and<br>implementation of cutting edge technologies in Cloud Data Analytics &amp; AI.</p>
  </section>

  <section class="slide centered workshop" style="left:515px; top:324px;">
    <div class="brand" style="top:30px;"><span class="brand-mark"></span><span class="brand-name">lumafox</span></div>
    <h2>About the Workshop</h2>
    <p class="objective">The objective of this workshop is for you to discover<br>feasible and high-impact AI use cases.</p>
    <div class="pillars">
      <div class="pillar">
        <svg viewBox="0 0 30 28" fill="none" stroke="#04253a" stroke-width="1.8"><circle cx="15" cy="6" r="4"/><circle cx="6" cy="9" r="3"/><circle cx="24" cy="9" r="3"/><path d="M9 25v-7a6 6 0 0 1 12 0v7z"/><path d="M2 25v-6a4 4 0 0 1 6-3.4M28 25v-6a4 4 0 0 0-6-3.4M2 25h26"/></svg>
        <span>You, not us.</span>
      </div>
      <div class="pillar">
        <svg viewBox="0 0 30 28" fill="none" stroke="#04253a" stroke-width="1.8"><path d="M6 1h14l5 5v21H6z"/><path d="M9 8l2 2 3-3M9 15l2 2 3-3M9 22l2 2 3-3M16 9h6M16 16h6M16 23h6"/></svg>
        <span>Feasible,<br>not impossible</span>
      </div>
      <div class="pillar">
        <svg viewBox="0 0 30 28" fill="none" stroke="#04253a" stroke-width="1.8"><rect x="3" y="19" width="5" height="7"/><rect x="12" y="15" width="5" height="11"/><rect x="21" y="11" width="5" height="15"/><path d="M3 13l7-6 5 4 10-9M20 2h5v5"/></svg>
        <span>High impact</span>
      </div>
    </div>
  </section>

  <section class="slide" style="left:51px; top:600px;">
    <div class="slide-header">
      <div class="brand"><span class="brand-mark"></span><span class="brand-name">lumafox</span></div>
      <span class="header-divider"></span>
      <span class="header-title">Agenda</span>
    </div>
    <div class="agenda-steps">
      <div class="step inspire"><strong>Inspire</strong><small>(60 minutes)</small></div>
      <div class="step discover"><strong>Discover</strong><small>(60 minutes)</small></div>
      <div class="step prioritize"><strong>Prioritize</strong><small>(90 minutes)</small></div>
    </div>
  </section>

  <section class="slide definition ai-def" style="left:518px; top:603px;">
    <div class="slide-header">
      <div class="brand"><span class="brand-mark"></span><span class="brand-name">lumafox</span></div>
      <span class="header-divider"></span>
      <span class="header-title">Artificial Intelligence</span>
    </div>
    <div class="photo" role="img" aria-label="Illustration of a digital head made of blue circuit lines"></div>
    <p class="definition-text">It is the general field of computer science dedicated to creating machines that can simulate human intelligence.</p>
  </section>

  <section class="slide definition ml-def" style="left:51px; top:876px;">
    <div class="slide-header">
      <div class="brand"><span class="brand-mark"></span><span class="brand-name">lumafox</span></div>
      <span class="header-divider"></span>
      <span class="header-title">Machine Learning</span>
    </div>
    <div class="photo" role="img" aria-label="Photo of hands typing on a laptop surrounded by floating code screens"></div>
    <p class="definition-text">Machine learning is a subfield of artificial intelligence that focuses on enabling machines to learn from data using algorithms without being explicitly programmed for each task.</p>
  </section>

  <section class="slide closing" style="left:515px; top:876px;">
    <div class="brand"><span class="brand-mark"></span><span class="brand-name">lumafox</span></div>
    <h2>Thank You</h2>
  </section>

</main>
</body>
</html>
```